Finding Amber Gate Keepers (Book cover)

This project is for a book I am currently writing. It will help pastors and church leaders communicate why serving in the local church is the so important and how to motivate them to serve at high levels.

The title of the book comes from the passage of scripture where Jesus said, "when a solider demands you to carry his gear one mile, go with him two." He wants his followers to willingly do more than is expected. Doing the minimum seldom does much to change hearts of people around us.

This book will deal with these concepts and help leaders train others to follow in this line of thinking - to be Amber Gate Keepers.

Target Market(s)

church leaders, christian book readers

Industry/Entity Type

Church

Font styles to use
Sans Serif

Colors
fece3e

Requirements
Must have
• Catchy color, font layout to attract readers to take a 2nd look inside the book. Lots of empty space on the cover art, gradient color, sharp contrasts. Large Letters
Nice to have
• A central image on the artwork that will communicate the metaphor of going the 2nd mile.
Should not have
• any imagery that is suggestive

```html
<!DOCTYPE html>
<html lang="en">
<head>
<meta charset="utf-8">
<title>Amber Gate Keepers — Book Cover</title>
<link href="https://fonts.googleapis.com/css2?family=Black+Ops+One&family=Handlee&family=Kaushan+Script&display=swap" rel="stylesheet">
<style>
  :root {
    --page-bg: #efebe4;
    --title-yellow: #fece3e;
    --ink-dark: #1c1608;
    --author-rust: #b8683c;
    --photo-deep: #17130a;
    --photo-mid: #5a4a1f;
    --photo-warm: #9a8236;
    --photo-glow: #d8bd63;
  }
  html, body {
    margin: 0;
    padding: 0;
    width: 1200px;
    height: 730px;
    overflow: hidden;
    background: var(--page-bg);
  }
  .book-cover {
    position: absolute;
    left: 370px;
    top: 20px;
    width: 460px;
    height: 690px;
    overflow: hidden;
    box-shadow: 0 10px 30px rgba(0,0,0,0.25);
  }
  .cover-photo {
    position: absolute;
    inset: 0;
    width: 100%;
    height: 100%;
  }
  .cover-title {
    position: absolute;
    left: 26px;
    top: 28px;
    margin: 0;
    font-family: "Black Ops One", sans-serif;
    font-weight: 400;
    font-size: 74px;
    line-height: 0.98;
    color: var(--title-yellow);
    text-transform: uppercase;
    letter-spacing: 1px;
  }
  .cover-title span { display: block; }
  .scripture-quote {
    position: absolute;
    left: 36px;
    right: 20px;
    top: 300px;
    margin: 0;
    white-space: nowrap;
    font-family: "Handlee", cursive;
    font-size: 12.5px;
    color: var(--ink-dark);
  }
  .quote-source {
    position: absolute;
    right: 30px;
    top: 326px;
    margin: 0;
    font-family: "Kaushan Script", cursive;
    font-size: 26px;
    color: var(--ink-dark);
  }
  .author-name {
    position: absolute;
    left: 24px;
    right: 24px;
    bottom: 34px;
    margin: 0;
    display: flex;
    justify-content: space-between;
    font-family: "Black Ops One", sans-serif;
    font-size: 26px;
    color: var(--author-rust);
  }
</style>
</head>
<body>
  <div class="book-cover">
    <svg class="cover-photo" viewBox="0 0 460 690" preserveAspectRatio="none" role="img" aria-label="Sepia-toned photograph of a wooden cross pendant above a lit candle standing among dark saucers">
      <defs>
        <linearGradient id="photoTone" x1="0" y1="0" x2="0" y2="1">
          <stop offset="0" stop-color="var(--photo-deep)"/>
          <stop offset="0.3" stop-color="var(--photo-mid)"/>
          <stop offset="0.55" stop-color="var(--photo-warm)"/>
          <stop offset="0.75" stop-color="var(--photo-mid)"/>
          <stop offset="1" stop-color="var(--photo-deep)"/>
        </linearGradient>
        <radialGradient id="candleGlow" cx="0.6" cy="0.7" r="0.35">
          <stop offset="0" stop-color="var(--photo-glow)" stop-opacity="0.55"/>
          <stop offset="1" stop-color="var(--photo-glow)" stop-opacity="0"/>
        </radialGradient>
      </defs>
      <rect width="460" height="690" fill="url(#photoTone)"/>
      <rect width="460" height="690" fill="url(#candleGlow)"/>
    </svg>

    <h1 class="cover-title"><span>Amber</span><span>Gate</span><span>Keepers</span></h1>

    <p class="scripture-quote">"when a solider demands you to carry his gear one mile, go with him two"</p>
    <p class="quote-source">– Elias Marron</p>

    <p class="author-name"><span>A</span><span>U</span><span>T</span><span>H</span><span>O</span><span>R</span><span>N</span><span>A</span><span>M</span><span>E</span></p>
  </div>
</body>
</html>
```